Design Business Card Aerial Drone Photography

we need a business card that shows we are a leader in:
-Aerial Videos
-Aerial Photography
-Aerial Real Estate Photography
the attached logo is in blue, however please feel free to submit creative colors and designs
Updates

I would like to add the words "Veteran Owned and Operated" to my business card Certified Drone Operator should appear as one line Thanks, Ned Corliss

Target Market(s)

real estate, cell towers, companies that want to showcase their company with aerial drone photography

Contact Information for Business Card

logo files have been submitted in pdf, jpg, png, .ai, .eps., .svg formats. Please feel free to be creative with design and colors, possibly a cloud type background
sample attached.
review my website www.brightwrenaerial.example that should help with designing my business card
Services:
-Aerial Videos
-Aerial Photography

Font styles to use
Sans Serif

Colors

Designer to choose colors to be used in the design.

Requirements
Must have
• company logo
• Bright Wren Aerial
• Ned Corliss Certified Drone Operator
• 555-619-4827
• brightwrenaerial@mailbox.example
• www.brightwrenaeriel.example
• 2971 Maplewood Ln, Dunwoody GA 30338
Nice to have
• Please feel free to be creative with design and colors

```html
<!DOCTYPE html>
<html lang="en">
<head>
<meta charset="utf-8">
<title>Bright Wren Aerial – Business Cards</title>
<link rel="stylesheet" href="https://fonts.googleapis.com/css2?family=Roboto:wght@400;500;700&display=swap">
<style>
  :root {
    --page: #2b2b2d;
    --card: #ffffff;
    --brand: #1768b3;
    --brand-soft: #3f86c6;
    --sky-top: #b9d6f2;
    --sky-mid: #e3effa;
    --photo-harbor-a: #2b8fb0;
    --photo-harbor-b: #8fb9c4;
    --photo-estate-a: #6f8a4e;
    --photo-estate-b: #9a7a62;
    --photo-coast-a: #2f79c0;
    --photo-coast-b: #a58a72;
    --photo-store-a: #5fa0de;
    --photo-store-b: #b49878;
  }
  * { box-sizing: border-box; margin: 0; padding: 0; }
  html, body { width: 1200px; height: 900px; overflow: hidden; }
  body {
    background: var(--page);
    font-family: "Roboto", Arial, sans-serif;
    position: relative;
  }
  .card {
    position: absolute;
    width: 513px;
    height: 296px;
    border-radius: 20px;
    overflow: hidden;
    background: var(--card);
    box-shadow: 0 6px 14px rgba(0,0,0,.45);
  }
  .card--front { left: 73px; top: 138px; }
  .card--back-a { left: 615px; top: 138px; }
  .card--back-b { left: 73px; top: 465px; }
  .card--back-c { left: 615px; top: 465px; }

  .sky {
    background:
      radial-gradient(ellipse 160px 60px at 80% 14%, rgba(255,255,255,.85), transparent 70%),
      radial-gradient(ellipse 200px 70px at 30% 28%, rgba(255,255,255,.7), transparent 70%),
      radial-gradient(ellipse 140px 50px at 60% 45%, rgba(255,255,255,.6), transparent 70%),
      linear-gradient(180deg, var(--sky-top) 0%, var(--sky-mid) 45%, #ffffff 72%);
  }

  /* front photo grid */
  .photo { position: absolute; }
  .photo--harbor { left: 0; top: 0; width: 256px; height: 145px;
    background: linear-gradient(135deg, var(--photo-harbor-b), var(--photo-harbor-a)); }
  .photo--estate { left: 262px; top: 0; width: 251px; height: 145px;
    background: linear-gradient(160deg, #7ea3c9 0%, var(--photo-estate-a) 30%, var(--photo-estate-b) 100%); }
  .photo--coast { left: 0; top: 151px; width: 256px; height: 145px;
    background: linear-gradient(170deg, var(--photo-coast-a) 0%, var(--photo-coast-a) 40%, var(--photo-coast-b) 100%); }
  .photo--store { left: 262px; top: 151px; width: 251px; height: 145px;
    background: linear-gradient(180deg, var(--photo-store-a) 0%, #9ec6ea 35%, var(--photo-store-b) 100%); }
  .front-badge {
    position: absolute; left: 188px; top: 78px;
    width: 142px; height: 142px; border-radius: 50%;
    background: #fff;
    display: flex; align-items: center; justify-content: center;
    flex-direction: column; gap: 6px;
  }

  /* brand lockup */
  .brand { position: absolute; display: flex; flex-direction: column; gap: 5px; }
  .brand__row { display: flex; align-items: center; gap: 7px; }
  .brand__dot { width: 14px; height: 14px; border-radius: 50%; background: var(--brand); flex: none; }
  .brand__name {
    color: var(--brand); font-weight: 700; font-size: 18px;
    text-transform: uppercase; letter-spacing: .2px; white-space: nowrap;
  }
  .brand__tagline {
    color: var(--brand-soft); font-size: 10px; letter-spacing: .6px;
    text-transform: uppercase; border-top: 1px solid var(--brand-soft); padding-top: 5px;
  }
  .front-badge .brand__name { font-size: 13px; }

  .services { position: absolute; list-style: none; color: var(--brand); font-size: 11.5px; font-weight: 500; line-height: 14.5px; }
  .services li { padding-left: 8px; text-indent: -8px; }
  .services li::before { content: "• "; }

  .person { position: absolute; color: var(--brand); text-transform: uppercase; }
  .person__name { font-size: 13.5px; font-weight: 500; line-height: 17px; }
  .person__title { font-size: 11px; font-weight: 700; line-height: 15px; }
  .rule { position: absolute; height: 1px; background: var(--brand); }

  .contacts { position: absolute; list-style: none; color: var(--brand); font-size: 11.5px; font-weight: 500; line-height: 14.5px; text-transform: uppercase; }
  .contacts li { display: flex; align-items: center; gap: 6px; white-space: nowrap; }
  .contacts svg { width: 10px; height: 10px; flex: none; }
</style>
</head>
<body>

<!-- Front -->
<section class="card card--front">
  <div class="photo photo--harbor" role="img" aria-label="Aerial photo of a marina with rows of docked boats"></div>
  <div class="photo photo--estate" role="img" aria-label="Aerial photo of a large house among trees"></div>
  <div class="photo photo--coast" role="img" aria-label="Aerial photo of a coastal hillside town and ocean"></div>
  <div class="photo photo--store" role="img" aria-label="Aerial photo of a retail store building"></div>
  <div class="front-badge">
    <span class="brand__dot"></span>
    <span class="brand__name">Bright Wren Aerial</span>
  </div>
</section>

<!-- Back A -->
<section class="card card--back-a sky">
  <div class="brand" style="left:39px;top:82px;">
    <div class="brand__row"><span class="brand__dot"></span><span class="brand__name">Bright Wren Aerial</span></div>
    <div class="brand__tagline">Veteran Owned and Operated</div>
  </div>
  <ul class="services" style="left:340px;top:53px;">
    <li>Aerial Videos</li><li>Aerial Photography</li><li>Aerial Real Estate Photography</li>
  </ul>
  <div class="person" style="left:39px;top:184px;">
    <div class="person__name">Ned Corliss</div>
    <div class="person__title">Certified Drone Operator</div>
  </div>
  <div class="rule" style="left:212px;top:207px;width:265px;"></div>
  <ul class="contacts" style="left:39px;top:231px;">
    <li><svg viewBox="0 0 10 10"><circle cx="5" cy="5" r="4.5" fill="none" stroke="currentColor"/><path d="M3 3.2c.4 2 1.8 3.4 3.8 3.8l.4-.9-1-.5-.5.5c-.8-.3-1.5-1-1.8-1.8l.5-.5-.5-1z" fill="currentColor"/></svg>555 619 4827</li>
    <li><svg viewBox="0 0 10 10"><circle cx="5" cy="5" r="4.5" fill="currentColor"/><rect x="2.6" y="3.4" width="4.8" height="3.4" fill="#fff"/><path d="M2.6 3.4L5 5.3l2.4-1.9" stroke="currentColor" stroke-width=".6" fill="none"/></svg>brightwrenaerial@mailbox.example</li>
    <li><svg viewBox="0 0 10 10"><circle cx="5" cy="5" r="4.5" fill="none" stroke="currentColor"/><ellipse cx="5" cy="5" rx="1.8" ry="4.5" fill="none" stroke="currentColor" stroke-width=".6"/><path d="M.5 5h9" stroke="currentColor" stroke-width=".6"/></svg>www.brightwrenaeriel.example</li>
  </ul>
</section>

<!-- Back B -->
<section class="card card--back-b sky">
  <div class="brand" style="left:39px;top:82px;">
    <div class="brand__row"><span class="brand__dot"></span><span class="brand__name">Bright Wren Aerial</span></div>
    <div class="brand__tagline">Veteran Owned and Operated</div>
  </div>
  <ul class="services" style="left:341px;top:53px;">
    <li>Aerial Videos</li><li>Aerial Photography</li><li>Aerial Real Estate Photography</li>
  </ul>
  <div class="person" style="left:39px;top:231px;">
    <div class="person__name">Ned Corliss</div>
    <div class="person__title">Certified Drone Operator</div>
  </div>
  <ul class="contacts" style="left:255px;top:231px;">
    <li><svg viewBox="0 0 10 10"><circle cx="5" cy="5" r="4.5" fill="none" stroke="currentColor"/><path d="M3 3.2c.4 2 1.8 3.4 3.8 3.8l.4-.9-1-.5-.5.5c-.8-.3-1.5-1-1.8-1.8l.5-.5-.5-1z" fill="currentColor"/></svg>555 619 4827</li>
    <li><svg viewBox="0 0 10 10"><circle cx="5" cy="5" r="4.5" fill="currentColor"/><rect x="2.6" y="3.4" width="4.8" height="3.4" fill="#fff"/><path d="M2.6 3.4L5 5.3l2.4-1.9" stroke="currentColor" stroke-width=".6" fill="none"/></svg>brightwrenaerial@mailbox.example</li>
    <li><svg viewBox="0 0 10 10"><circle cx="5" cy="5" r="4.5" fill="none" stroke="currentColor"/><ellipse cx="5" cy="5" rx="1.8" ry="4.5" fill="none" stroke="currentColor" stroke-width=".6"/><path d="M.5 5h9" stroke="currentColor" stroke-width=".6"/></svg>www.brightwrenaeriel.example</li>
  </ul>
</section>

<!-- Back C -->
<section class="card card--back-c sky">
  <div class="brand" style="right:36px;top:82px;align-items:flex-end;">
    <div class="brand__row"><span class="brand__dot"></span><span class="brand__name">Bright Wren Aerial</span></div>
    <div class="brand__tagline">Veteran Owned and Operated</div>
  </div>
  <div class="person" style="left:39px;top:184px;">
    <div class="person__name">Ned Corliss</div>
    <div class="person__title">Certified Drone Operator</div>
  </div>
  <div class="rule" style="left:212px;top:207px;width:265px;"></div>
  <ul class="contacts" style="left:39px;top:231px;">
    <li><svg viewBox="0 0 10 10"><circle cx="5" cy="5" r="4.5" fill="none" stroke="currentColor"/><path d="M3 3.2c.4 2 1.8 3.4 3.8 3.8l.4-.9-1-.5-.5.5c-.8-.3-1.5-1-1.8-1.8l.5-.5-.5-1z" fill="currentColor"/></svg>555 619 4827</li>
    <li><svg viewBox="0 0 10 10"><circle cx="5" cy="5" r="4.5" fill="currentColor"/><rect x="2.6" y="3.4" width="4.8" height="3.4" fill="#fff"/><path d="M2.6 3.4L5 5.3l2.4-1.9" stroke="currentColor" stroke-width=".6" fill="none"/></svg>brightwrenaerial@mailbox.example</li>
    <li><svg viewBox="0 0 10 10"><circle cx="5" cy="5" r="4.5" fill="none" stroke="currentColor"/><ellipse cx="5" cy="5" rx="1.8" ry="4.5" fill="none" stroke="currentColor" stroke-width=".6"/><path d="M.5 5h9" stroke="currentColor" stroke-width=".6"/></svg>www.brightwrenaeriel.example</li>
  </ul>
  <ul class="services" style="left:340px;top:220px;">
    <li>Aerial Videos</li><li>Aerial Photography</li><li>Aerial Real Estate Photography</li>
  </ul>
</section>

</body>
</html>
```